Etiketten-Design für Weine
Die Zusammenarbeit hat viel Freude gemacht. Kompetent, kreativ...ich bin mit dem Ergebnis sehr zufrieden!
Zielgruppe
Wir sind ein kleines Familien-Weingut Nahe Bernkastel-Kues an der Mosel. Wir erzeugen auf 5,5ha ca. 40-50 TSD Flaschen Wein. Dabei legen wir Wert auf eine naturnahe Bewirtschaftung und eine gute Qualität der Weine. Die wichtigste Rebsorte ist der Riesling. Ansonsten steht die Mosel vor allem für Schieferstein, Steillagen, schöne Landschaft. Die Vermarktung erfolgt fast ausschließlich an Privatkunden. Die Kunden sind i. d. R. mind. 40 Jahre bis 70 Jahre alt gehören mind. der Mittelschicht an; Akademiker und Personen mit Dr.-Titel sind stärker repräsentiert als im Bundesdurchschnitt. Die Vermarktung ist stark Personengebunden: Ich als Winzer bin meist persönlich im Gespräch mit den Kunden.
Aufgabenstellung
Bei dem Entwurf geht es mehr um eine 'kleinen Relaunch'. Bevor Anfang Januar 2021 neue Etiketten gedruckt werden für den neuen Jahrgang, soll das Design nochmals überdacht werden. Hin und wieder werde ich angesprochen von Seiten der Kundschaft; das bisherige Etikett wird anscheinend eher als altbacken wahrgenommen.
Grundsätzlich besteht das Etikett aus dem Logo (farbiger Balken, Hauszeichnung, Schriftzug Brandauer-Kossek) und dem weißen Feld mit der Weinbezeichnung darunter. Für den goldenen Rahmen und den Schriftzug Brandauer-Kossek wird Heißfolienprägung verwendet. Grün=Basisweine/Literflasche; rot=Hauptlinie ; lila=Premiumlinie ; schwarz=nur für den Rotwein ; Emil am Bach (Perlwein) ist ein Sonderetikett mit einem Acrylbild und der Sonnwerk Traubensaft erhält jedes Jahr eine neues Foto der Traubenleser. Die stets verwendete Schriftart ist Windows Garamond.
Grundsätzlich würde ich an dem Logo (farbiger Balken mit Hauszeichnung und Schriftzug Weingut Brandauer-Kossek) eigentlich gerne festhalten. Da dieses Logo bereits überall Verwendung findet (Broschüre, Visitenkarten, Briefbogen, Weingläser, Weinstand, Website, etc.). Lediglich der goldene Rahmen steht zur Disposition (der findet - außer beim Etikett - sonst keine Verwendung). Gestaltungsmöglichkeit sehe ich in dem weißen Feld unter dem Logo. Da bin ich für alles offen. Mögliche Ansatzpunkte wären Herkunft oder Personen oder einfach grafische Elemente/Effekte um das Etikett aufzuwerten. Da ich bereits mit den verschiedenen Farben (grün/rot/lila/schwarz) arbeite, würde ich an dieser Stelle nicht zusätzlich weitere Farben ins Spiel bringen. Wichtig sind mir die prägnanten Weinnamen (Hofgeflüster, Nebel Neun, Feuerglut, Goldener Krug, usw.) Die gesetzlich notwendigen Angaben befinden sich jedoch auf dem Rückenetikett. Das gesamte Weinsortiment kann auch angeschaut werden im Shop unter www.brandauer-kossek-wein.de

```html
<!DOCTYPE html>
<html lang="de">
<head>
<meta charset="utf-8">
<title>Weinetiketten – Weingut Brandauer-Kossek</title>
<link rel="stylesheet" href="https://fonts.googleapis.com/css2?family=EB+Garamond:ital,wght@0,400;0,500;1,400&display=swap">
<style>
  :root {
    --canvas: #dcdcdc;
    --paper: #ffffff;
    --ink: #111111;
    --gold: #9b7e5c;
    --band-text: #e9e6e1;
    --line-black: #000000;
    --line-purple: #352235;
    --line-green: #115e4a;
    --line-red: #67242b;
    --special-red: #a03535;
    --serif: "EB Garamond", Garamond, "Times New Roman", serif;
  }
  * { box-sizing: border-box; margin: 0; padding: 0; }
  html, body { width: 988px; height: 1200px; overflow: hidden; }
  body { background: var(--canvas); font-family: var(--serif); color: var(--ink); }

  .label-sheet {
    display: grid;
    grid-template-columns: repeat(2, 440px);
    grid-template-rows: repeat(3, 330px);
    column-gap: 36px;
    row-gap: 40px;
    padding: 65px 36px;
  }

  .label { position: relative; width: 440px; height: 330px; background: var(--paper); overflow: hidden; }
  .label--black  { --band: var(--line-black); }
  .label--purple { --band: var(--line-purple); }
  .label--green  { --band: var(--line-green); }
  .label--red    { --band: var(--line-red); }
  .label--special{ --band: var(--special-red); }

  .brand-band { position: absolute; left: 0; top: 0; width: 100%; height: 157px; background: var(--band); }
  .label--special .brand-band { height: 257px; }

  .estate-house {
    position: absolute; left: 50%; top: 13px; width: 86px; height: 60px;
    transform: translateX(-50%);
    background: rgba(255,255,255,.2);
  }

  .estate-kicker {
    position: absolute; left: 0; right: 0; top: 98px;
    display: flex; justify-content: center; align-items: center; gap: 10px;
    font-size: 15px; letter-spacing: .25em; color: var(--band-text); line-height: 1;
  }
  .estate-kicker::before, .estate-kicker::after {
    content: ""; width: 36px; height: 1px; background: var(--band-text);
  }
  .estate-name {
    position: absolute; left: 0; right: 0; top: 111px;
    text-align: center; font-size: 34px; color: var(--gold); line-height: 1; letter-spacing: .01em;
  }

  .foil-rule { position: absolute; left: 0; width: 100%; background: var(--gold); }
  .foil-rule--thin  { top: 159px; height: 4px; }
  .foil-rule--thick { top: 166px; height: 6px; }

  .wine-name {
    position: absolute; left: 0; right: 0; top: 184px;
    text-align: center; font-weight: 400; font-size: 33px; line-height: 1;
    text-transform: uppercase; letter-spacing: .02em;
  }
  .wine-name .initial { font-size: 43px; }
  .wine-name--twoline { top: 176px; line-height: .92; }
  .grape {
    position: absolute; left: 0; right: 0; top: 236px;
    text-align: center; font-size: 19px; letter-spacing: .1em; line-height: 1; text-transform: uppercase;
  }
  .taste {
    position: absolute; left: 50%; top: 270px; width: 168px; transform: translateX(-50%);
    text-align: center; font-style: italic; font-size: 16px; line-height: 1;
    padding-bottom: 4px; border-bottom: 1px solid var(--ink);
  }
  .vintage {
    position: absolute; left: 0; right: 0; top: 298px;
    text-align: center; font-size: 15px; line-height: 1;
  }

  .label--special .painting {
    position: absolute; left: 110px; top: 0; width: 220px; height: 180px;
    background: linear-gradient(180deg, #5f93b8 0%, #c9d4d8 38%, #eef0ee 55%, #2f6b4d 100%);
  }
  .label--special .estate-kicker { top: 196px; }
  .label--special .estate-name { top: 210px; }
  .label--special .foil-rule--thin  { top: 259px; }
  .label--special .foil-rule--thick { top: 266px; }
  .label--special .wine-name { top: 286px; }
</style>
</head>
<body>
<main class="label-sheet">

  <article class="label label--black">
    <div class="brand-band"></div>
    <div class="estate-house" role="img" aria-label="Hauszeichnung des Weinguts"></div>
    <p class="estate-kicker">WEINGUT</p>
    <p class="estate-name">Brandauer-Kossek</p>
    <div class="foil-rule foil-rule--thin"></div>
    <div class="foil-rule foil-rule--thick"></div>
    <h2 class="wine-name"><span class="initial">N</span>ebel <span class="initial">N</span>eun</h2>
    <p class="grape">Riesling</p>
    <p class="taste">trocken</p>
    <p class="vintage">2020</p>
  </article>

  <article class="label label--purple">
    <div class="brand-band"></div>
    <div class="estate-house" role="img" aria-label="Hauszeichnung des Weinguts"></div>
    <p class="estate-kicker">WEINGUT</p>
    <p class="estate-name">Brandauer-Kossek</p>
    <div class="foil-rule foil-rule--thin"></div>
    <div class="foil-rule foil-rule--thick"></div>
    <h2 class="wine-name"><span class="initial">G</span>oldener <span class="initial">K</span>rug</h2>
    <p class="grape">Riesling</p>
    <p class="taste">trocken</p>
    <p class="vintage">2020</p>
  </article>

  <article class="label label--green">
    <div class="brand-band"></div>
    <div class="estate-house" role="img" aria-label="Hauszeichnung des Weinguts"></div>
    <p class="estate-kicker">WEINGUT</p>
    <p class="estate-name">Brandauer-Kossek</p>
    <div class="foil-rule foil-rule--thin"></div>
    <div class="foil-rule foil-rule--thick"></div>
    <h2 class="wine-name"><span class="initial">S</span>teillage</h2>
    <p class="grape">Riesling</p>
    <p class="taste">trocken</p>
    <p class="vintage">2020</p>
  </article>

  <article class="label label--red">
    <div class="brand-band"></div>
    <div class="estate-house" role="img" aria-label="Hauszeichnung des Weinguts"></div>
    <p class="estate-kicker">WEINGUT</p>
    <p class="estate-name">Brandauer-Kossek</p>
    <div class="foil-rule foil-rule--thin"></div>
    <div class="foil-rule foil-rule--thick"></div>
    <h2 class="wine-name"><span class="initial">H</span>ofgeflüster</h2>
    <p class="grape">Weissburgunder</p>
    <p class="taste">trocken</p>
    <p class="vintage">2020</p>
  </article>

  <article class="label label--red">
    <div class="brand-band"></div>
    <div class="estate-house" role="img" aria-label="Hauszeichnung des Weinguts"></div>
    <p class="estate-kicker">WEINGUT</p>
    <p class="estate-name">Brandauer-Kossek</p>
    <div class="foil-rule foil-rule--thin"></div>
    <div class="foil-rule foil-rule--thick"></div>
    <h2 class="wine-name wine-name--twoline"><span class="initial">F</span>rohsinn<br><span class="initial">J</span>ohanniter</h2>
    <p class="taste">feinherb</p>
    <p class="vintage">2020</p>
  </article>

  <article class="label label--special">
    <div class="brand-band"></div>
    <div class="painting" role="img" aria-label="Acrylbild mit weißen Gänsen auf grüner Wiese vor blauem Himmel"></div>
    <p class="estate-kicker">WEINGUT</p>
    <p class="estate-name">Brandauer-Kossek</p>
    <div class="foil-rule foil-rule--thin"></div>
    <div class="foil-rule foil-rule--thick"></div>
    <h2 class="wine-name"><span class="initial">E</span>mil am <span class="initial">B</span>ach</h2>
  </article>

</main>
</body>
</html>
```